Create a Eye Catching Flyerr for my online business

I would like an eye catching flyer with the relevant content for my business.

This flyer is to advertise my online business and the call to action is to get Butchers to sign up to my online site to start selling their products.

the flyer must be eye catching, each to understand, easy to read and relevant to the audience being local butcher shops.

Attached is the marketing packs with all the required information about the business The flyer must not be too long, but the front page must be catching and want the audience to read more. It must very direct, targeted and focused on the audience

It mus be duplicate sides

Reason: need a little more time for review

Industry/Entity Type

Marketing

Font styles to use
Serif
Sans Serif

Colors
9bcb3b
ffffff
fee18a
fac994
f37122
f78f20
ffc214

```html
<!DOCTYPE html>
<html lang="en">
<head>
<meta charset="utf-8">
<title>Prime Cut Market – Butcher Sign-Up Flyer</title>
<link rel="stylesheet" href="https://fonts.googleapis.com/css2?family=Bebas+Neue&family=Raleway:wght@500;600;700&display=swap">
<style>
  :root {
    --stage: #2a2a2a;
    --paper: #e9e9ea;
    --green: #5e9132;
    --green-dark: #3f6b1d;
    --green-light: #9bcb3b;
    --ink: #1e1e1e;
    --white: #ffffff;
    --food-warm: #d9a25a;
    --food-deep: #8a5a2b;
    --food-fresh: #7fa94a;
  }
  * { box-sizing: border-box; margin: 0; padding: 0; }
  html, body { width: 1200px; height: 900px; overflow: hidden; }
  body { background: var(--stage); font-family: "Raleway", sans-serif; color: var(--ink); position: relative; }

  .page { position: absolute; background: var(--paper); overflow: hidden; box-shadow: 0 6px 18px rgba(0,0,0,.5); }
  .page--front { left: 60px; top: 70px; width: 522px; height: 758px; }
  .page--back { left: 622px; top: 72px; width: 532px; height: 754px; }
  .page svg.shapes { position: absolute; left: 0; top: 0; }

  .headline { font-family: "Bebas Neue", sans-serif; font-weight: 400; }

  /* front */
  .brand { position: absolute; left: 18px; top: 300px; width: 220px; text-align: center;
    font-family: "Raleway", sans-serif; font-weight: 700; font-size: 17px; letter-spacing: 1px; color: var(--ink); }
  .feature-rail { position: absolute; left: 430px; top: 328px; width: 66px; height: 360px; background: var(--green); }
  .feature { position: absolute; left: 18px; width: 440px; height: 78px; background: var(--green);
    border-radius: 40px 0 0 40px; border-top: 3px solid var(--white); color: var(--white);
    padding: 10px 50px 0 18px; line-height: 1.05; }
  .feature .headline { font-size: 40px; vertical-align: -2px; }
  .feature .lead { font-size: 15.5px; font-weight: 500; }
  .feature--welcome { top: 354px; }
  .feature--offer { top: 460px; }
  .feature--benefits { top: 564px; }
  .thumb { position: absolute; border-radius: 50%; border: 4px solid var(--white);
    box-shadow: 0 2px 5px rgba(0,0,0,.35);
    background: radial-gradient(circle at 45% 45%, var(--food-warm), var(--food-deep)); }
  .page--front .thumb { width: 86px; height: 86px; left: 422px; }
  .tagline { position: absolute; left: 0; right: 0; bottom: 12px; text-align: center;
    font-size: 33px; color: var(--green-light); }

  /* back */
  .hero-back { position: absolute; left: 0; top: 0; width: 532px; height: 210px;
    background: linear-gradient(135deg, #5a3a22 0%, #c9934f 45%, #e9c27a 60%, #8fae4f 85%, #b5412b 100%); }
  .page--back .thumb.t1 { left: 36px; top: 140px; width: 112px; height: 112px; }
  .page--back .thumb.t2 { left: 208px; top: 158px; width: 120px; height: 120px; }
  .page--back .thumb.t3 { left: 382px; top: 128px; width: 120px; height: 120px; }
  .badge { position: absolute; left: 380px; top: 266px; width: 136px; height: 136px; border-radius: 50%;
    background: var(--green); color: var(--white); display: flex; flex-direction: column;
    align-items: center; justify-content: center; transform: rotate(-35deg); line-height: .95; }
  .badge .small { font-size: 15px; font-weight: 500; }
  .badge .headline { font-size: 24px; }
  .packages-tab { position: absolute; left: 0; top: 283px; width: 222px; height: 60px; background: var(--green);
    border-radius: 0 30px 30px 0; color: var(--white); font-size: 46px; padding: 4px 0 0 20px; }
  .package { position: absolute; left: 20px; width: 420px; }
  .package h3 { color: var(--green); font-size: 20px; font-weight: 600; margin-bottom: 6px; }
  .package .sub { font-size: 14.5px; font-weight: 700; margin-bottom: 3px; }
  .package p { font-size: 15px; font-weight: 500; line-height: 1.45; }
  .package--banner { top: 354px; }
  .package--turnkey { top: 452px; }
  .signup-title { position: absolute; left: 50px; right: 28px; top: 556px; display: flex; align-items: center; gap: 12px;
    color: var(--green); font-size: 48px; }
  .signup-title::before, .signup-title::after { content: ""; flex: 1; height: 3px; background: var(--green-dark); }
  .signup-copy { position: absolute; left: 20px; right: 14px; top: 604px; font-size: 15px; font-weight: 500; line-height: 1.45; }
  .contact-email { position: absolute; left: 0; right: 0; bottom: 8px; text-align: center; font-size: 42px; color: var(--green-light); }
</style>
</head>
<body>

<section class="page page--front">
  <svg class="shapes" width="522" height="758" viewBox="0 0 522 758">
    <circle cx="390" cy="90" r="258" fill="var(--green)"/>
    <circle cx="392" cy="80" r="244" fill="url(#heroFront)" role="img" aria-label="Photo of a crumbed fish fillet with roast potatoes, salad and lemon"/>
    <defs>
      <radialGradient id="heroFront" cx="50%" cy="40%" r="60%">
        <stop offset="0" stop-color="#e8b466"/>
        <stop offset=".6" stop-color="#c98f45"/>
        <stop offset="1" stop-color="#7a9a3c"/>
      </radialGradient>
    </defs>
    <circle cx="118" cy="195" r="100" fill="var(--white)"/>
    <circle cx="118" cy="195" r="94" fill="var(--green)"/>
    <path d="M0 650 C 150 690, 360 700, 522 668 L522 758 L0 758 Z" fill="var(--white)"/>
    <path d="M0 658 C 150 700, 360 708, 522 676 L522 758 L0 758 Z" fill="var(--green-dark)"/>
  </svg>
  <div class="brand">PRIME CUT MARKET</div>

  <div class="feature-rail"></div>
  <div class="feature feature--welcome"><span class="headline">Welcome to</span> <span class="lead">the new digital age. Think of all the big global online businesses.</span></div>
  <div class="feature feature--offer"><span class="headline">What we offer</span> <span class="lead">Prime Cut Market aim to offer the following to signed up members</span></div>
  <div class="feature feature--benefits"><span class="headline">Customer benefits</span> <span class="lead">Having an online presence and shopping portal to</span></div>
  <div class="thumb" style="top:352px" role="img" aria-label="Photo of grilled fish fillets"></div>
  <div class="thumb" style="top:458px" role="img" aria-label="Photo of a plated fish dish"></div>
  <div class="thumb" style="top:562px" role="img" aria-label="Photo of a crumbed fillet with salad"></div>

  <div class="tagline headline">A world of opportunity</div>
</section>

<section class="page page--back">
  <div class="hero-back" role="img" aria-label="Photo of fish and chips with salad on a white plate"></div>
  <svg class="shapes" width="532" height="754" viewBox="0 0 532 754">
    <path d="M0 170 C 150 230, 380 225, 532 150 L532 182 C 380 250, 150 260, 0 200 Z" fill="var(--green)"/>
    <path d="M0 200 C 150 260, 380 250, 532 182 L532 240 L0 240 Z" fill="var(--paper)"/>
    <path d="M0 662 C 180 690, 380 680, 532 632 L532 754 L0 754 Z" fill="var(--white)"/>
    <path d="M0 670 C 180 698, 380 688, 532 640 L532 754 L0 754 Z" fill="var(--green-dark)"/>
  </svg>
  <div class="thumb t1" role="img" aria-label="Photo of grilled fish with lemon"></div>
  <div class="thumb t2" role="img" aria-label="Photo of a white fish fillet with vegetables"></div>
  <div class="thumb t3" role="img" aria-label="Photo of salmon with tomatoes"></div>

  <div class="badge"><span class="small">Start Now</span><span class="headline">There are</span><span class="headline">no contracts</span></div>

  <div class="packages-tab headline">Packages</div>
  <div class="package package--banner">
    <h3>Home Page Banner</h3>
    <div class="sub">For Extra Exposure</div>
    <p>Ads Must be booked in advance &amp; price is not Inclusive of Design Creation</p>
  </div>
  <div class="package package--turnkey">
    <h3>Complete turn key solution</h3>
    <div class="sub">For hassle free start up</div>
    <p>Ads Must be booked in advance &amp; price is not Inclusive of Design Creation</p>
  </div>

  <div class="signup-title headline">I want to sign up</div>
  <p class="signup-copy">If you are interested in joining the revolution, the process is very simple.Simply send an email to the address below notifying us of that you are interested in signing up</p>

  <div class="contact-email headline">support@primecutmarket.com.au</div>
</section>

</body>
</html>
```